Business Card Design For A Renovation Contractor Company

We need a business card for a new company based in Singapore, our company name is "KT Planora". We are a renovation contractor that builds designs into reality. We build more of F&B restaurants, retail stores and commercial offices. We work very closely with designers. The final design should communicate to our client that we are a company that you can trust, that will plan and complete your project without giving you a headache. I like my client to remember my company as "KT". The beauty of SIMPLE is important.

Industry/Entity Type

Contractor

Requirements
Nice to have
• Black or Red base

```html
<!DOCTYPE html>
<html lang="en">
<head>
<meta charset="utf-8">
<title>KT Planora Business Card</title>
<link rel="stylesheet" href="https://fonts.googleapis.com/css2?family=Oswald:wght@500;600&family=Open+Sans:wght@400;600&display=swap">
<style>
  :root {
    --stage: #3b4350;
    --stage-edge: #2f3a4a;
    --card-light: #ececec;
    --bar-grey: #7a7a7a;
    --accent: #d8411f;
    --ink: #2b2b2b;
    --ink-soft: #4a4a4a;
    --card-dark: #2a2d32;
    --silver-hi: #ffffff;
    --silver-lo: #8a9191;
    --brand-red: #c4262b;
  }
  * { box-sizing: border-box; margin: 0; padding: 0; }
  html, body { width: 1200px; height: 1000px; overflow: hidden; }
  body {
    background: linear-gradient(135deg, var(--stage-edge), var(--stage) 55%, var(--stage-edge));
    position: relative;
    font-family: "Open Sans", Arial, sans-serif;
  }
  .card {
    position: absolute;
    left: 320px;
    width: 560px;
    height: 320px;
    overflow: hidden;
    box-shadow: 0 14px 30px rgba(0,0,0,0.45);
  }
  /* Front */
  .card--front { top: 140px; background: var(--card-light); }
  .front__side-bar { position: absolute; left: 0; top: 0; width: 38px; height: 100%; background: var(--bar-grey); }
  .front__corner-block { position: absolute; right: 0; top: 28px; width: 40px; height: 52px; background: var(--bar-grey); }
  .front__name-block { position: absolute; right: 58px; top: 34px; text-align: right; }
  .front__name { font-family: "Oswald", sans-serif; font-weight: 600; font-size: 28px; line-height: 1; color: var(--accent); letter-spacing: 0.5px; }
  .front__role { font-size: 11px; font-weight: 600; color: var(--ink-soft); margin-top: 2px; }
  .front__band-long { position: absolute; left: 360px; right: 0; top: 150px; height: 26px; background: var(--accent); }
  .front__band-short { position: absolute; left: 38px; width: 68px; top: 200px; height: 22px; background: var(--accent); }
  .front__company { position: absolute; left: 112px; top: 162px; font-family: "Oswald", sans-serif; font-weight: 500; font-size: 44px; line-height: 1; color: var(--ink); letter-spacing: 0.5px; }
  .front__contacts { position: absolute; left: 118px; top: 234px; font-size: 12.5px; color: var(--ink-soft); line-height: 1.7; }
  .contact-row { display: flex; align-items: flex-start; gap: 9px; }
  .contact-row svg { flex: none; margin-top: 4px; }
  .contact-row + .contact-row { margin-top: 6px; }
  .highlight { color: var(--accent); }
  /* Back */
  .card--back { top: 540px; background: var(--card-dark); }
  .back__silver-band {
    position: absolute; left: 0; right: 0; top: 92px; height: 136px;
    background: linear-gradient(90deg, var(--silver-lo) 0%, var(--silver-hi) 35%, var(--silver-hi) 60%, var(--silver-lo) 100%);
    display: flex; align-items: center; justify-content: center; gap: 12px;
  }
  .brand-dot { width: 22px; height: 22px; border-radius: 50%; background: var(--brand-red); }
  .brand-name { font-family: "Open Sans", sans-serif; font-weight: 600; font-size: 34px; color: var(--brand-red); letter-spacing: 0.5px; }
</style>
</head>
<body>
  <section class="card card--front" aria-label="Business card front">
    <div class="front__side-bar"></div>
    <div class="front__corner-block"></div>
    <div class="front__name-block">
      <p class="front__name">MARCUS LIM.</p>
      <p class="front__role">Position Director</p>
    </div>
    <div class="front__band-long"></div>
    <div class="front__band-short"></div>
    <h1 class="front__company">KT PLANORA</h1>
    <div class="front__contacts">
      <div class="contact-row">
        <svg width="10" height="13" viewBox="0 0 10 13"><path d="M5 0C2.2 0 0 2.2 0 5c0 3.5 5 8 5 8s5-4.5 5-8c0-2.8-2.2-5-5-5z" fill="#e8862f"/><circle cx="5" cy="5" r="1.8" fill="#ececec"/></svg>
        <p>8 Keppel Lane ,#03-210<br>Keppel Trade Hub ,<strong>Singapore</strong> 098765</p>
      </div>
      <div class="contact-row">
        <svg width="12" height="10" viewBox="0 0 12 10"><rect x="0.5" y="0.5" width="11" height="9" rx="1" fill="none" stroke="#e8862f"/><path d="M0.5 1l5.5 4.5L11.5 1" fill="none" stroke="#e8862f"/></svg>
        <p>marcus@<span class="highlight">ktplanora</span>.com</p>
      </div>
    </div>
  </section>

  <section class="card card--back" aria-label="Business card back">
    <div class="back__silver-band">
      <span class="brand-dot"></span>
      <span class="brand-name">KT Planora</span>
    </div>
  </section>
</body>
</html>
```